Thank You For Shopping / Hair Care Tips

I need “Thank You For Shopping”
Post cards made for my hair business !
I added pictures of post cards that I really like . I also added my LunaVex Wigs logo for you guys to use

I want the backside of the flyer to have hair care tips !
I want people to have full directions on how to care for their wigs

Target Market(s)

Im marking to young woman to older middle aged woman
Ages 23-66 . I want my flyer to look mature And classy

Industry/Entity Type

Hair And Beauty

Font styles to use
Serif
Script

Colors
e34699
e34298
e34398

Requirements
Must have
• The flyer must have the Instagram logo with my Instagram name next to it @luna.vex.wigs__
• Also it must have my “Luna Vex Wigs” logo that I’ve uploaded in the pictures section .
• Flyer had to be two sides . One side “ thank you for shopping “ side two “hair care tips”
• My website must be on the flyer - www.lunavexwigs.example
• The flyer must match the colors of my logo
• All white . With the pink and glitter sliver you see on my logo
Nice to have
• Nice to have a glitter border
Should not have
• The flyer should not have different colors that don’t match my logo
• It shouldn’t be made without having my Instagram or website on the flyer

```html
<!DOCTYPE html>
<html lang="en">
<head>
<meta charset="utf-8">
<title>Luna Vex Wigs – Thank You Postcard</title>
<link rel="stylesheet" href="https://fonts.googleapis.com/css2?family=Great+Vibes&family=Allura&family=Playfair+Display:wght@700&family=Roboto+Condensed:ital,wght@0,400;1,400&family=Arimo:wght@700&display=swap">
<style>
  :root {
    --sheet: #ffffff;
    --mat-mauve: #c4a3b6;
    --pink: #e34398;
    --pink-deep: #d62f88;
    --magenta: #c014c4;
    --violet: #7c0a82;
    --ink: #000000;
    --text: #2a2a2a;
    --white: #ffffff;
    --hair-grey: #6f6a68;
  }
  * { margin: 0; padding: 0; box-sizing: border-box; }
  html, body { width: 1200px; height: 849px; overflow: hidden; background: var(--sheet); }
  .sheet { position: relative; width: 1200px; height: 849px; }

  /* ---------- Front ---------- */
  .card-front {
    position: absolute; left: 124px; top: 238px; width: 451px; height: 301px;
    background: var(--mat-mauve);
  }
  .card-front__panel {
    position: absolute; left: 13.5px; top: 14px; width: 423.5px; height: 273px;
    background: linear-gradient(180deg, var(--magenta) 0%, var(--violet) 38%, #2a0530 68%, var(--ink) 82%);
    overflow: hidden;
  }
  .front-hair {
    position: absolute; left: 150px; top: 0; width: 139px; height: 225px;
    border-radius: 60px 60px 30px 30px;
    background: radial-gradient(ellipse at 50% 30%, rgba(220,90,220,.28), rgba(60,10,60,.18) 60%, transparent 75%);
  }
  .thank-you {
    position: absolute; left: 14px; top: 28px;
    font-family: 'Great Vibes', cursive; color: var(--pink);
    font-size: 66px; line-height: 54px;
  }
  .thank-you span { display: block; }
  .thank-you .you { padding-left: 38px; }
  .shopping-line {
    position: absolute; left: 162px; top: 88px;
    font-family: 'Allura', cursive; color: var(--white); font-size: 30px;
  }
  .front-brand {
    position: absolute; right: 14px; top: 164px; text-align: right;
    font-family: 'Playfair Display', serif; font-weight: 700; color: var(--pink);
    font-size: 30px; line-height: 32px;
  }
  .front-contact {
    position: absolute; left: 12px; bottom: 8px; display: flex; align-items: center; gap: 22px;
    font-family: 'Roboto Condensed', sans-serif; font-style: italic; color: var(--white); font-size: 7.6px;
  }
  .social { display: flex; align-items: center; gap: 3px; }
  .social__dot { width: 9px; height: 9px; border-radius: 50%; background: var(--pink); }

  /* ---------- Back ---------- */
  .card-back {
    position: absolute; left: 603px; top: 238px; width: 451px; height: 301px;
    background: linear-gradient(135deg, var(--pink-deep), var(--pink) 50%, var(--pink-deep));
  }
  .card-back__panel {
    position: absolute; left: 14px; top: 14px; width: 423px; height: 273px;
    background: #fdfdfd; overflow: hidden;
  }
  .back-hair {
    position: absolute; left: 0; top: 0; width: 153px; height: 174px;
    background: radial-gradient(ellipse at 45% 20%, var(--hair-grey) 0%, rgba(140,135,132,.55) 45%, rgba(255,255,255,0) 78%);
  }
  .tips-heading {
    position: absolute; font-family: 'Great Vibes', cursive; color: var(--pink); font-size: 22px;
  }
  .tips-heading--hair { left: 177px; top: 10px; }
  .tips-heading--wig { left: 146px; top: 133px; }
  .tips-rule { position: absolute; height: 1px; background: var(--pink); }
  .tips-rule--hair { left: 177px; top: 36px; width: 234px; }
  .tips-rule--wig { left: 146px; top: 160px; width: 144px; }
  .tips-list {
    position: absolute; list-style: none;
    font-family: 'Roboto Condensed', sans-serif; color: var(--text);
    font-size: 7.3px; line-height: 9.5px;
  }
  .tips-list--hair { left: 196px; top: 53px; }
  .tips-list--wig { left: 154px; top: 182px; }
  .back-brand {
    position: absolute; left: 10px; top: 164px;
    font-family: 'Playfair Display', serif; font-weight: 700; color: var(--pink);
    font-size: 26px; line-height: 28px;
  }

  .side-label {
    position: absolute; top: 578px; width: 200px; text-align: center;
    font-family: 'Arimo', sans-serif; font-weight: 700; font-size: 16px; color: var(--text);
  }
  .side-label--front { left: 251px; }
  .side-label--back { left: 728px; }
</style>
</head>
<body>
<main class="sheet">
  <section class="card-front">
    <div class="card-front__panel">
      <div class="front-hair" role="img" aria-label="Faint photo of a long wavy wig"></div>
      <h1 class="thank-you"><span>Thank</span><span class="you">You</span></h1>
      <p class="shopping-line">for shopping with us!</p>
      <div class="front-brand">Luna Vex<br>Wigs</div>
      <div class="front-contact">
        <span class="website">www.lunavexwigs.example</span>
        <span class="social"><span class="social__dot"></span>@luna.vex.wigs__</span>
      </div>
    </div>
  </section>

  <section class="card-back">
    <div class="card-back__panel">
      <div class="back-hair" role="img" aria-label="Photo of a long wavy brunette wig fading into white"></div>
      <h2 class="tips-heading tips-heading--hair">Hair Care Tips</h2>
      <div class="tips-rule tips-rule--hair"></div>
      <ul class="tips-list tips-list--hair">
        <li>- Wash with lukewarm water.</li>
        <li>- Condition correctly</li>
        <li>- Be extra thorough with rinsing</li>
        <li>- Don't dry off using a towel.</li>
        <li>- Blow-dry with a brush</li>
        <li>- Give strands a break from ponytails.</li>
        <li>- Deep condition regularly</li>
        <li>- Air dry when you can</li>
      </ul>
      <h2 class="tips-heading tips-heading--wig">Wig Care Tips</h2>
      <div class="tips-rule tips-rule--wig"></div>
      <ul class="tips-list tips-list--wig">
        <li>- After washing a wig, do not shake it in a towel.</li>
        <li>- While washing your hair, never use shampoo meant for natural hair.</li>
        <li>- Condition your hair every couple weeks or so, to keep it shiny and soft.</li>
        <li>- Wigs should only be washed with special shampoo made just for wigs.</li>
        <li>- Brush your wig with a wig brush before washing.</li>
        <li>- Avoid rubbing against things that create friction, which can be damaging to a wig.</li>
        <li>- Do not brush or touch your wig when it is wet from water, steam, rain, snow etc.</li>
        <li>- Do not rub, twist, or wring your wig.</li>
      </ul>
      <div class="back-brand">Luna Vex<br>Wigs</div>
    </div>
  </section>

  <p class="side-label side-label--front">Front</p>
  <p class="side-label side-label--back">Back</p>
</main>
</body>
</html>
```